Private practice for psychiatry and psychotherapy needs a business card and logo

I need a logo and business card design for my private practice for psychiatry and psychotherapy. The optional names for my practice are: Vornhoute Praktijk voor Psychiatrie en Psychotherapie, or short: Praktijk Vornhoute.
I am a (child and adolescent) psychiatrist and psychotherapist. I diagnose and treat infants, children, adolescents and adults with psychiatric symptoms/disorders. I also give supervision to colleagues about their own treatments. My work is characterised by personal involvement, transparence, creativity and professionality.
I would like to have an appealing, light and bright, yet basic design that invites people (both children and adults) to contact me, gives trust and hope, without loosing professional appearance.
I uploaded my contact information which should not necessarily be all included (in this form) on the card as long as people know how to contact me. Please feel free to be creative!
Please note that my website is only temporarely and need a new design and update too!

Target Market(s)

Clients and patients (children, adolescents, adults) with psychiatric symptoms who need diagnosis and treatment. I work with private clients and patients through medical insurances.

Industry/Entity Type

Mental Health

Contact Information for Business Card

Dr. Sanne Vornhoute-ter Kuilen
Psychiater/Kinder- en Jeugdpsychiater
Wouter Heskampstraat 14
3071 PX Rotterdam
t: 06-51928764
e: info@praktijkvornhoute.nl
i: www.praktijkvornhoute.nl

Logo Text

Praktijk Vornhoute voor Psychiatrie en Psychotherapie; or short: Praktijk Vornhoute

Font styles to use
Sans Serif
Other font styles liked:
• up to designer

Requirements
Must have
• Appealing, light, bright, creative, trustful, professional and unique.

```html
<!DOCTYPE html>
<html lang="nl">
<head>
<meta charset="utf-8">
<title>Praktijk Vornhoute – visitekaartje</title>
<link rel="stylesheet" href="https://fonts.googleapis.com/css2?family=Raleway:wght@300;400;500;700;800&display=swap">
<style>
  :root {
    --backdrop: #e4e4e4;
    --paper: #ffffff;
    --sun: #f2c123;
    --leaf: #5db83d;
    --slate: #7c7c7c;
    --ink-light: #ffffff;
  }
  html, body {
    margin: 0;
    padding: 0;
    width: 1200px;
    height: 1200px;
    overflow: hidden;
    background: var(--backdrop);
    font-family: "Raleway", sans-serif;
  }
  .sheet {
    position: relative;
    width: 1200px;
    height: 1200px;
  }
  .card {
    position: absolute;
    width: 520px;
    height: 335px;
    box-sizing: border-box;
    overflow: hidden;
  }
  .card--front {
    left: 56px;
    top: 330px;
    background: var(--paper);
  }
  .card--back {
    left: 624px;
    top: 330px;
    background: var(--sun);
  }
  .brand {
    position: absolute;
    left: 0;
    right: 0;
    top: 0;
    bottom: 0;
    display: flex;
    align-items: center;
    justify-content: center;
    gap: 18px;
  }
  .brand__dot {
    width: 34px;
    height: 34px;
    border-radius: 50%;
    background: var(--sun);
  }
  .brand__name {
    font-weight: 700;
    font-size: 34px;
    color: var(--leaf);
    letter-spacing: 0.2px;
  }
  .contact {
    position: absolute;
    left: 47px;
    top: 66px;
  }
  .contact__name {
    margin: 0;
    font-weight: 700;
    font-size: 21px;
    color: var(--ink-light);
  }
  .contact__role {
    margin: 4px 0 0;
    font-weight: 400;
    font-size: 18px;
    color: var(--ink-light);
  }
  .contact__details {
    margin: 34px 0 0;
    font-weight: 500;
    font-size: 16px;
    line-height: 23px;
    color: var(--leaf);
  }
  .contact__label { font-weight: 800; }
  .back-accent {
    position: absolute;
    right: 40px;
    bottom: -30px;
    width: 190px;
    height: 190px;
    border-radius: 50%;
    background: rgba(200, 150, 20, 0.18);
  }
  .specs {
    position: absolute;
    left: 624px;
    top: 730px;
    display: flex;
    gap: 40px;
    font-size: 27px;
    line-height: 36px;
  }
  .specs__swatches { font-weight: 800; }
  .specs__swatch--sun { color: var(--sun); }
  .specs__swatch--leaf { color: var(--leaf); }
  .specs__font-label { font-weight: 800; color: var(--slate); }
  .specs__font-name { font-weight: 400; color: var(--slate); }
</style>
</head>
<body>
<main class="sheet">
  <section class="card card--front" aria-label="Voorzijde visitekaartje">
    <div class="brand">
      <span class="brand__dot" aria-hidden="true"></span>
      <span class="brand__name">Praktijk Vornhoute</span>
    </div>
  </section>

  <section class="card card--back" aria-label="Achterzijde visitekaartje">
    <span class="back-accent" aria-hidden="true"></span>
    <div class="contact">
      <p class="contact__name">Dr. Sanne Vornhoute-ter Kuilen</p>
      <p class="contact__role">Psychiater/Kinder - en Jeugdpsychiater</p>
      <p class="contact__details">
        Wouter Heskampstraat 14<br>
        3071 PX Rotterdam<br>
        <span class="contact__label">t:</span> 06-51928764<br>
        <span class="contact__label">e:</span> info@praktijkvornhoute.nl<br>
        <span class="contact__label">i:</span> www.praktijkvornhoute.nl
      </p>
    </div>
  </section>

  <aside class="specs">
    <div class="specs__swatches">
      <div class="specs__swatch--sun">Kleur 7406U</div>
      <div class="specs__swatch--leaf">Kleur 368U</div>
    </div>
    <div>
      <div class="specs__font-label">Font family:</div>
      <div class="specs__font-name">Raleway</div>
    </div>
  </aside>
</main>
</body>
</html>
```